"Sketch Onward Club" Social Art Website Design

I need a design for a website I am building, which will be called Sketch Onward Club. I have attached the selected logo for the site. The site will be about drawing/art, and how art can be used to brighten a stranger's day as a random act of kindness. In real life, people will receive a drawing or piece of art with details for this site on it. They will in turn be able to give a drawing or piece of art to someone else, thus building a 'chain' of people who are related to each other through the drawings they have received. This should create a strong 'social' aspect to the site. There will be areas of the site for seeing other drawings/art that have been submitted, as well as for seeing different statistics (how many drawings have been submitted, where, how people are connected, etc.).

Target Market(s)

No specific target market.

Industry/Entity Type

Building

Coding

Number of Pages Required

1 page

Font styles to use
Sans Serif
Decorative

Requirements
Must have
• Must use the logo supplied.
Nice to have
• Should be colourful and artistic. References to art tools should be primarily around drawing, though painting can also feature. Colour scheme to match the logo would be ideal.

```html
<!DOCTYPE html>
<html lang="en">
<head>
<meta charset="utf-8">
<title>Sketch Onward Club</title>
<link rel="stylesheet" href="https://fonts.googleapis.com/css2?family=Patrick+Hand&family=Open+Sans:wght@400;600&display=swap">
<style>
:root{
  --pink:#f4287f;
  --blue:#3cbad2;
  --blue-dark:#2fa9c2;
  --orange:#fbb034;
  --orange-dark:#f3a632;
  --ink:#333;
  --muted:#888;
  --line:#e6e6e6;
  --hero-shade:#f0f0f2;
  --map:#dcdcdc;
  --white:#fff;
}
*{box-sizing:border-box;margin:0;padding:0}
html,body{width:712px;height:1200px;overflow:hidden;background:var(--white)}
body{position:relative;font-family:"Open Sans",Arial,sans-serif;color:var(--ink)}
.hand{font-family:"Patrick Hand",cursive}
.abs{position:absolute}

/* header */
.brand{left:53px;top:14px;display:flex;align-items:center;gap:5px;font-family:"Patrick Hand",cursive;font-size:12px;line-height:12px;color:var(--ink);width:80px}
.brand-dot{width:10px;height:10px;border-radius:50%;background:var(--pink);flex:none}
.nav{left:172px;top:21px;display:flex;gap:15px;font-family:"Patrick Hand",cursive;font-size:9px;color:#666;text-transform:uppercase}
.nav span{display:flex;align-items:center;gap:3px}
.nav .active{color:var(--pink);position:relative}
.nav .active::before{content:"";position:absolute;left:6px;top:-21px;width:30px;height:2px;background:var(--pink)}
.nav svg{width:9px;height:9px}
.signin{left:608px;top:16px;width:52px;height:22px;background:var(--blue);border:1px solid #2a8ea3;border-radius:2px;color:#fff;font-size:7px;display:flex;align-items:center;justify-content:center;gap:3px;box-shadow:0 1px 0 #1f7a8c}

/* hero */
.hero{left:0;top:0;width:712px;height:294px;overflow:hidden}
.hero-shade{left:0;top:0}
.hero-art{left:340px;top:62px;width:325px;height:232px;background:linear-gradient(160deg,#f5f5f7 0%,#e9f6fa 55%,#8fd8ea 100%)}
.welcome{left:53px;top:116px;font-size:20px;color:var(--ink)}
.title{left:53px;top:138px;font-size:27px;line-height:32px}
.title .b{color:var(--blue)} .title .o{color:var(--orange)}
.find-btn{left:53px;top:178px;width:75px;height:21px;border:1px solid var(--blue);color:var(--blue);font-family:"Patrick Hand",cursive;font-size:8px;display:flex;align-items:center;justify-content:center;gap:5px;border-radius:1px}
.dots{left:53px;top:256px;display:flex;gap:3px}
.dots i{width:4px;height:4px;border-radius:50%;background:#f7a6c8;display:block}
.dots i:first-child{width:9px;border-radius:3px;background:var(--pink)}
.pager{font-size:6px;color:#999;display:flex;align-items:center;gap:3px}

/* belief */
.belief{left:0;top:294px;width:712px;height:141px;background:var(--pink)}
.belief-art{left:88px;top:280px;width:92px;height:162px;background:linear-gradient(180deg,#8a5a3a 0%,#f6d7b0 35%,#fde7a0 60%,#e8e8e8 100%);border-radius:40px 40px 8px 8px}
.belief h2{left:218px;top:316px;font-family:"Patrick Hand",cursive;font-weight:400;font-size:13px;color:#fff}
.belief p{left:218px;top:337px;width:392px;font-size:7.8px;line-height:14.2px;color:#fff}

/* artwork */
.section-title{left:0;width:712px;text-align:center;font-family:"Patrick Hand",cursive;font-size:12.5px;color:#999}
.card{top:480px;height:186px;background:#fff;box-shadow:0 0 4px rgba(0,0,0,.12)}
.card .pic{position:absolute;left:3px;top:2px;right:3px;height:107px}
.card .name{position:absolute;top:124px;width:100%;text-align:center;font-family:"Patrick Hand",cursive;font-size:10px;color:var(--ink)}
.card .by{position:absolute;top:138px;width:100%;text-align:center;font-size:6.5px;color:#999}
.card hr{position:absolute;left:14px;right:14px;top:159px;border:0;border-top:1px solid var(--line)}
.card svg{position:absolute;left:50%;top:167px;margin-left:-4px;width:8px;height:8px}

/* stats */
.stats-l{left:0;top:683px;width:356px;height:148px;background:var(--orange)}
.stats-l-low{left:0;top:773px;width:356px;height:58px;background:var(--orange-dark)}
.stats-r{left:356px;top:683px;width:356px;height:148px;background:var(--blue);overflow:hidden}
.people-art{left:52px;top:708px;width:84px;height:94px;background:linear-gradient(180deg,#c98a5a,#e45a7e 45%,#4fb2d6 70%,#333 100%);border-radius:30px 30px 4px 4px}
.doc-art{left:547px;top:707px;width:113px;height:103px;background:linear-gradient(135deg,#222 0%,#222 40%,#fff 41%,#f2f2f2 100%)}
.stat{top:730px;width:139px;height:55px;background:#fff;border-radius:2px;display:flex;align-items:center;padding-left:13px;gap:10px}
.stat b{display:block;font-family:"Patrick Hand",cursive;font-weight:400;font-size:26px;line-height:22px;color:var(--ink)}
.stat small{display:block;font-family:"Patrick Hand",cursive;font-size:7.5px;color:#888}

/* map */
.map{left:0;top:831px;width:712px;height:165px;background:linear-gradient(160deg,#dadada 0%,#e2e2e2 70%,#0ba6b5 71%,#0aa0b0 100%)}

/* contact */
.contact-title{left:54px;top:1012px;font-family:"Patrick Hand",cursive;font-size:13px;color:#777}
.field{height:22px;border:1px solid var(--line);display:flex;align-items:center;gap:5px;padding-left:7px;font-family:"Patrick Hand",cursive;font-size:7.5px;color:#888}
.field svg{width:6px;height:6px}
.message{align-items:flex-start;padding-top:7px}
.send{left:53px;top:1124px;width:51px;height:21px;background:var(--blue);border:1px solid #2a8ea3;color:#fff;font-size:7px;display:flex;align-items:center;justify-content:center;gap:4px;box-shadow:0 1px 0 #1f7a8c;border-radius:1px}
.coder-art{left:520px;top:1025px;width:142px;height:144px;background:linear-gradient(180deg,#f3f3f3 0%,#f3f3f3 20%,#7a4a2a 21%,#f6d7b0 45%,#3cbad2 70%,#1e1e1e 100%);border-radius:60px 60px 6px 6px}

/* footer */
.footer{left:0;top:1169px;width:712px;height:31px;background:var(--pink);color:#fff;font-family:"Patrick Hand",cursive;font-size:8px;padding:12px 0 0 54px}
.to-top{left:638px;top:1160px;width:22px;height:22px;border-radius:50%;background:var(--orange);border:2px solid #fff;display:flex;align-items:center;justify-content:center}
</style>
</head>
<body>

<section class="hero abs">
  <svg class="hero-shade abs" width="712" height="294" aria-hidden="true"><polygon points="405,0 712,0 712,294 274,294" fill="var(--hero-shade)"/></svg>
  <div class="hero-art abs" role="img" aria-label="Illustration of two hands holding a greeting card with a heart of drawings, with coloured pens"></div>
  <div class="welcome abs hand">Welcome to</div>
  <div class="title abs hand"><span class="b">Sketch Onward</span> <span class="o">Club</span></div>
  <div class="find-btn abs">Find a Drawing
    <svg width="8" height="6" viewBox="0 0 8 6"><path d="M0 3h7M5 1l2 2-2 2" stroke="currentColor" fill="none" stroke-width=".8"/></svg></div>
  <div class="dots abs"><i></i><i></i><i></i></div>
  <div class="pager abs" style="left:15px;top:150px"><svg width="9" height="9" viewBox="0 0 9 9"><path d="M8 1L1 4.5 8 8z" fill="none" stroke="#aaa" stroke-width=".8"/></svg>Prev</div>
  <div class="pager abs" style="left:672px;top:150px;color:var(--pink)">Next<svg width="9" height="9" viewBox="0 0 9 9"><path d="M1 1l7 3.5L1 8z" fill="var(--pink)"/></svg></div>
</section>

<header>
  <div class="brand abs"><span class="brand-dot"></span>Sketch Onward Club</div>
  <nav class="nav abs">
    <span class="active"><svg viewBox="0 0 10 10"><path d="M1 5L5 1l4 4v4H1z" fill="none" stroke="currentColor"/></svg>Home</span>
    <span><svg viewBox="0 0 10 10"><path d="M4 0h2v8L5 10 4 8z" fill="none" stroke="currentColor"/></svg>Find a Drawing</span>
    <span><svg viewBox="0 0 10 10"><circle cx="5" cy="5" r="3" fill="none" stroke="currentColor" stroke-width="1.5" stroke-dasharray="1.5 1"/></svg>About</span>
    <span><svg viewBox="0 0 10 10"><circle cx="5" cy="5" r="4" fill="none" stroke="currentColor"/></svg>FAQ</span>
    <span><svg viewBox="0 0 10 10"><path d="M5 1v8" stroke="currentColor"/></svg>Report</span>
    <span><svg viewBox="0 0 10 10"><rect x="2" y="1" width="6" height="8" fill="none" stroke="currentColor"/></svg>Our Policies</span>
    <span><svg viewBox="0 0 10 10"><path d="M2 1l2 2-1 1c1 2 2 3 3 3l1-1 2 2-1 1C4 9 1 6 1 2z" fill="none" stroke="currentColor" stroke-width=".8"/></svg>Contact</span>
  </nav>
  <div class="signin abs"><svg width="6" height="6" viewBox="0 0 6 6"><circle cx="3" cy="1.6" r="1.4" fill="#fff"/><path d="M0 6c0-2 1.3-3 3-3s3 1 3 3z" fill="#fff"/></svg>Sign in</div>
</header>

<section class="belief abs"></section>
<div class="belief-art abs" role="img" aria-label="Cartoon painter in a beret holding a brush and palette"></div>
<div class="belief">
  <h2 class="abs">What we Believe</h2>
  <p class="abs">“We believe that the gift of hand-made art –a simple drawing with a nice message for a stranger can brighten somone’s day and make the world just a little bit better. We also believe everyone is an artist, whether or not you’ve had any training or thinkyou have anyartistic talent. We created Sketch Onward Club to join people together through art, creating an artistic chain of smiling people linked together through the simple act of drawing.”</p>
</div>

<h2 class="section-title abs" style="top:454px;font-weight:400">Recently Submited Artwork</h2>
<div class="pager abs" style="left:15px;top:569px"><svg width="9" height="9" viewBox="0 0 9 9"><path d="M8 1L1 4.5 8 8z" fill="none" stroke="#aaa" stroke-width=".8"/></svg>Prev</div>
<div class="pager abs" style="left:672px;top:569px">Next<svg width="9" height="9" viewBox="0 0 9 9"><path d="M1 1l7 3.5L1 8z" fill="none" stroke="#aaa" stroke-width=".8"/></svg></div>

<article class="card abs" style="left:50px;width:196px">
  <div class="pic" role="img" aria-label="Painting of tree silhouettes against an orange sunset" style="background:linear-gradient(180deg,#b33f00,#f6a000 45%,#3a1a00 100%)"></div>
  <div class="name">Art Title</div><div class="by">By: Mark Doe</div><hr>
  <svg viewBox="0 0 8 8"><circle cx="3.3" cy="3.3" r="2.5" fill="none" stroke="#bbb"/><path d="M5 5l2.5 2.5" stroke="#bbb"/></svg>
</article>
<article class="card abs" style="left:261px;width:191px">
  <div class="pic" role="img" aria-label="Painting of seagulls over crashing ocean waves" style="background:linear-gradient(180deg,#4a5fb0,#8fa6d8 45%,#2e5f86 70%,#e8eef2 100%)"></div>
  <div class="name">Art Title</div><div class="by">By: Mark Doe</div><hr>
  <svg viewBox="0 0 8 8"><circle cx="3.3" cy="3.3" r="2.5" fill="none" stroke="#bbb"/><path d="M5 5l2.5 2.5" stroke="#bbb"/></svg>
</article>
<article class="card abs" style="left:469px;width:191px">
  <div class="pic" role="img" aria-label="Painting of a lighthouse on a cliff under a pink sky" style="background:linear-gradient(180deg,#c85060,#f0a0a0 40%,#5e7a3a 70%,#b5a58a 100%)"></div>
  <div class="name">Art Title</div><div class="by">By: Mark Doe</div><hr>
  <svg viewBox="0 0 8 8"><circle cx="3.3" cy="3.3" r="2.5" fill="none" stroke="#bbb"/><path d="M5 5l2.5 2.5" stroke="#bbb"/></svg>
</article>

<section>
  <div class="stats-l abs"></div>
  <div class="stats-l-low abs"></div>
  <div class="stats-r abs"><svg width="356" height="148" aria-hidden="true"><polygon points="230,0 356,0 356,148 180,148" fill="var(--blue-dark)"/></svg></div>
  <div class="people-art abs" role="img" aria-label="Cartoon group of three friends"></div>
  <div class="doc-art abs" role="img" aria-label="Illustrated drawing sheet on a dark folder"></div>
  <div class="stat abs" style="left:182px">
    <svg width="22" height="18" viewBox="0 0 22 18"><circle cx="8" cy="5" r="4" fill="var(--orange)"/><circle cx="15" cy="6" r="3.5" fill="var(--orange)"/><path d="M0 18c0-5 3-8 8-8s8 3 8 8z" fill="var(--orange)"/><path d="M14 11c4 0 7 2 7 7h-4z" fill="var(--orange)"/></svg>
    <div><b>1.5K</b><small>Number of users</small></div>
  </div>
  <div class="stat abs" style="left:391px">
    <svg width="22" height="20" viewBox="0 0 22 20"><path d="M11 1C5 1 1 5 1 10s4 9 9 9c2 0 2-2 1-3s0-3 2-3h3c3 0 5-2 5-5 0-4-4-7-10-7z" fill="var(--blue)"/><circle cx="6" cy="9" r="1.6" fill="#fff"/><circle cx="9" cy="5" r="1.6" fill="#fff"/><circle cx="14" cy="5" r="1.6" fill="#fff"/></svg>
    <div><b>1.7K</b><small>Drawings Recieved</small></div>
  </div>
</section>

<section class="map abs" role="img" aria-label="Street map showing the club location">
  <svg class="abs" style="left:345px;top:62px" width="24" height="38" viewBox="0 0 24 38"><path d="M12 1a10 10 0 0 0-10 10c0 7 10 16 10 16s10-9 10-16A10 10 0 0 0 12 1z" fill="var(--white)" stroke="var(--pink)" stroke-width="3"/><circle cx="12" cy="36" r="2" fill="var(--pink)"/></svg>
</section>

<section>
  <h2 class="contact-title abs" style="font-weight:400">Contact us</h2>
  <div class="field abs" style="left:53px;top:1039px;width:144px"><svg viewBox="0 0 6 6"><circle cx="3" cy="1.6" r="1.4" fill="#bbb"/><path d="M0 6c0-2 1.3-3 3-3s3 1 3 3z" fill="#bbb"/></svg>Full name...</div>
  <div class="field abs" style="left:206px;top:1039px;width:144px"><svg viewBox="0 0 6 6"><rect x="0" y="1" width="6" height="4" fill="#bbb"/></svg>Email address...</div>
  <div class="field abs" style="left:357px;top:1039px;width:144px"><svg viewBox="0 0 6 6"><path d="M1 0l1.3 1.3-.7.7c.6 1.2 1.2 1.8 2.4 2.4l.7-.7L6 5 5 6C2 6 0 4 0 1z" fill="#bbb"/></svg>Cell number / Phone number</div>
  <div class="field message abs" style="left:53px;top:1071px;width:448px;height:42px"><svg viewBox="0 0 6 6"><rect x=".5" y=".5" width="5" height="4" fill="none" stroke="#bbb"/></svg>Type your message here...</div>
  <div class="send abs"><svg width="7" height="7" viewBox="0 0 7 7"><path d="M0 3l7-3-2 7-2-2z" fill="#fff"/></svg>Send</div>
  <div class="coder-art abs" role="img" aria-label="Cartoon man with glasses working at a laptop, with a paper plane"></div>
</section>

<footer class="footer abs">© 2016 Sketch Onward Club</footer>
<div class="to-top abs"><svg width="6" height="4" viewBox="0 0 6 4"><path d="M0 4l3-4 3 4z" fill="#fff"/></svg></div>

</body>
</html>
```